Stationery Design Project for Marketing Consultancy

I have started a new consultancy business and require the following elements to be designed using existing logo:
• Business card
• Letterhead
• Envelope (DL, C4, C5)
• Microsoft word template for report writing
• A4 Presentation Folder
• Powerpoint template
COPY FOR FRONT AND BACK OF BUSINESS CARD
logo
'Countable Growth. Bold Outcomes' slogan (but no need to use existing lockup with logo)
name, B Bus. Mktg, Grad Dip Digital Mktg, CPM (post nominal abbreviations in smaller font)
mobile: 04XX-XXX-XXX (I will give details to the winner to add)
website: www.quorvale.com.au
email: info@quorvale.com.au
COPY FOR LETTERHEAD
Logo
Company Name
Please, submit your designs that include business card, letterhead and envelope. Once selected the winner will be asked to complete the project by creating the rest of the artwork.
FINAL FILES
Print ready files to be supplied as well as Indesign files so that minor amends can be made if necessary in future.
• Layered vectors in EPS & PDF
• Screen quality JPEG & PNGs
ABOUT THE BUSINESS: QUORVALE
I work with clients to understand their business challenges, developing and executing measurable marketing strategies tied to key business metrics. Services include:
Services include:
• Business planning and business development
• Marketing and brand strategy
• Insight-driven integrated campaigns
• Loyalty programs and retention marketing
• Marketing automation
• Direct marketing (traditional and digital)
• Content strategy and development
Hi everyone,
Target Market(s)
Corporate decision makers (heads of marketing, general managers etc) and small to medium sized business owners. Predominately male aged 35+
Industry/Entity Type
Marketing
Requirements
Must have
- BRAND PERSONALITY
The successful design will communicate brand personality. I am a professional, results-driven entrepreneur, but want to show off my creative flair.
MEMORABILITY
Looking for a unique and eye-catching design. Am considering special printing effects (die cuts, letterpress, interactive elements, embossing, foiling etc) or a striking minimalist approach.
Nice to have
- I have a mission that could be incorporated on reverse if room -
Turning insights into actions & passion into profit.
Should not have
- Use of pink or green.

```html
<!DOCTYPE html>
<html lang="en">
<head>
<meta charset="utf-8">
<title>Quorvale Business Card</title>
<link href="https://fonts.googleapis.com/css2?family=Open+Sans:wght@400;600;700;800&family=Titillium+Web:wght@300&display=swap" rel="stylesheet">
<style>
  :root {
    --page-bg: #ededf0;
    --card-dark-inner: #5c5c5c;
    --card-dark-outer: #343434;
    --card-light: #ffffff;
    --ink-dark: #3d3d3d;
    --ink-mid: #5a5a5a;
    --ink-light: #ffffff;
    --accent-blue: #1a73c8;
    --divider: #b9b9b9;
  }
  * { box-sizing: border-box; margin: 0; padding: 0; }
  html, body { width: 1200px; height: 900px; overflow: hidden; }
  body {
    background: var(--page-bg);
    font-family: "Open Sans", Arial, sans-serif;
    display: flex;
    flex-direction: column;
    align-items: center;
    justify-content: center;
    gap: 56px;
  }
  .card {
    position: relative;
    width: 640px;
    height: 366px;
    border-radius: 26px;
    overflow: hidden;
    box-shadow: 0 10px 28px rgba(0,0,0,0.16);
  }
  .card--front {
    background: radial-gradient(ellipse at 50% 40%, var(--card-dark-inner) 0%, var(--card-dark-outer) 85%);
    color: var(--ink-light);
    display: flex;
    flex-direction: column;
    align-items: center;
    justify-content: center;
  }
  .brand {
    display: flex;
    flex-direction: column;
    align-items: center;
  }
  .brand__mark {
    display: flex;
    align-items: center;
    gap: 12px;
  }
  .brand__dot {
    width: 22px; height: 22px; border-radius: 50%;
    background: currentColor;
  }
  .brand__name {
    font-weight: 800;
    font-size: 52px;
    letter-spacing: 1px;
    line-height: 1;
  }
  .brand__slogan {
    margin-top: 8px;
    font-weight: 600;
    font-size: 12.5px;
    letter-spacing: 0.6px;
    text-transform: uppercase;
  }
  .card--front .website {
    margin-top: 44px;
    font-family: "Titillium Web", Arial, sans-serif;
    font-weight: 300;
    font-size: 30px;
    letter-spacing: 1px;
    color: #d8d8d8;
  }
  .card--back {
    background: var(--card-light);
    color: var(--ink-dark);
    display: flex;
    align-items: center;
  }
  .card--back .brand {
    width: 330px;
    align-items: center;
  }
  .card--back .brand__name { font-size: 40px; }
  .card--back .brand__dot { width: 18px; height: 18px; }
  .card--back .brand__slogan { font-size: 9.5px; }
  .divider {
    position: absolute;
    left: 330px; top: 96px;
    width: 1px; height: 150px;
    background: linear-gradient(to bottom, transparent, var(--divider) 30%, var(--divider) 70%, transparent);
  }
  .contact {
    padding-left: 34px;
    color: var(--ink-mid);
  }
  .contact__name {
    font-weight: 700;
    font-size: 22px;
    color: var(--accent-blue);
    line-height: 1.1;
  }
  .contact__role { font-size: 14px; margin-bottom: 12px; }
  .contact__credentials { font-size: 10.5px; margin-bottom: 8px; }
  .contact__line { font-size: 12px; line-height: 1.45; }
  .contact__line b { font-weight: 700; color: var(--ink-dark); }
  .accent-tab {
    position: absolute;
    right: 0; top: 250px;
    width: 40px; height: 48px;
    background: var(--accent-blue);
  }
</style>
</head>
<body>
  <section class="card card--front">
    <div class="brand">
      <div class="brand__mark">
        <span class="brand__dot"></span>
        <span class="brand__name">QUORVALE</span>
      </div>
      <p class="brand__slogan">Countable Growth. Bold Outcomes.</p>
    </div>
    <p class="website">www.quorvale.com.au</p>
  </section>

  <section class="card card--back">
    <div class="brand">
      <div class="brand__mark">
        <span class="brand__dot"></span>
        <span class="brand__name">QUORVALE</span>
      </div>
      <p class="brand__slogan">Countable Growth. Bold Outcomes.</p>
    </div>
    <span class="divider"></span>
    <div class="contact">
      <p class="contact__name">Your Name</p>
      <p class="contact__role">Principal</p>
      <p class="contact__credentials">B Bus. Mktg, Grad Dip Digital Mktg, CPM</p>
      <p class="contact__line"><b>Mobile:</b> 04XX-XXX-XXX</p>
      <p class="contact__line"><b>Email:</b> info@quorvale.com.au</p>
    </div>
    <span class="accent-tab"></span>
  </section>
</body>
</html>
```